We need a .psd design for a store we are creating called Bright Pouches. I will need only the main home page designed.

The store will be an eCommerce website that sells custom printed men's wallets. Customers will come onto the website and be able to upload their own images or add text to the front, back and inside of the wallet. We will initially be launching with one wallet style and will be expanding our range in the future for now the only images of a wallet on the website should be of the style attached.

There will be multiple templates that a customer can choose and edit the design of so there will effectively be a large number of products on display in the store. However, on the homepage there should just be a couple of featured products and the main emphasis should be on the features of the wallet/website and links to other areas of the website (customise your own wallet, edit our templates, bespoke designer wallets).

For the styling of the website, it needs to be funky and fresh with lots of colour. The logo of the website is attached and the styling should mirror the logo style.

The main features of the website should be on the home page. These features are:
- 5 year money back guarantee on wallet
- High quality, durable leather, made to last
- customer can upload photo and edit them online with our online picture editor
- 3d mockup of the wallet as you are designing it to show what it looks like with custom images on
- Edit any of our ready made wallet designs

Features of this wallet may be used as well - these can be viewed on "Image 6" of the attached product image .psd files.

Attached are the logo for the website and the wallet product photos. The product photos are provided in .psd format and have smart objects so that you can add any image to the front/inside of the wallets for any images on the website you create. Fee free to edit them and use them for banner images and feature images however you feel necessary.

The term "what does you wallet say about you" should be used as this is a tagline for most of the marketing - based on the fact that the wallets are personalised to each individual they will show off that individuals personality and what they like.

The eventual website will be hosted on cartnest and will more than likely use the "StallKit" theme. This is a highly adaptable theme and examples of the layout styles for the homepage can be found here: http://reef.lindolayouts.example/cartnest/stallkit-intro/?storefront=pixora-assets however i do not want you to just copy a ready made template and stick some stock photos in - I only want one page designing here, put the effort in with the banners and feature images and you'll win this.

Any images that you create for hero sliders/banners should be provided in .psd format so that they can be edited as necessary in the future. A newsletter popup should also be designed as the website will have postwren integration, the newsletter popup is a 500 x 750 image that pops up with a message saying "subscribe to our newsletter and get 10% off your next order".

There should also be an area of the page that has customer testimonials.

Target Market(s)

Males, aged 18 - 45

Industry/Entity Type

Retail

Number of Pages Required

1 page

Font styles to use
Serif
Decorative
Script

Colors

Designer to choose colors to be used in the design.

Requirements
Must have
• Vibrant and uplifting feel to the website
• Design which reflects the logo
• Features of the website and wallets should feature prominently on the homepage (but not in banner/hero image)
Nice to have
• hipster/geek/easygoing vibe
• Images that have used the wallet .psd files and have different designs on them showing customers that anything can be printed on the wallets
• Custom images/styles for the featured images and main banner.
Should not have
• - Boring images
• - Stock Photos
• - Mundane feel
• - Square block style images - try putting images in circles or geometric shapes with colours, just adding a stock photo to some "lorem Ipsum" text will not win you this contest

```html
<!DOCTYPE html>
<html lang="en">
<head>
<meta charset="utf-8">
<title>Bright Pouches – Custom Printed Men's Wallets</title>
<link rel="stylesheet" href="https://fonts.googleapis.com/css2?family=Roboto+Condensed:wght@300;400;700&family=Roboto:wght@400;500;700;900&display=swap">
<style>
:root{
  --red:#ee4323;
  --blue:#1aa0cf;
  --sky:#0ea5dd;
  --green:#12a558;
  --yellow:#f0d40d;
  --ink:#1e1f24;
  --dark:#23262d;
  --darker:#1b1d22;
  --grey:#f2f2f2;
  --grey-mid:#e2e2e2;
  --muted:#b9bcc3;
  --white:#ffffff;
  --head:"Roboto Condensed", "Arial Narrow", sans-serif;
  --body:"Roboto", Arial, sans-serif;
}
*{box-sizing:border-box;margin:0;padding:0}
html,body{width:1200px;height:3136px;overflow:hidden}
body{font-family:var(--body);color:var(--ink);background:var(--white)}
section,header,footer,.topbar,.bottombar{position:relative;width:1200px;overflow:hidden}
.abs{position:absolute}

/* top bar */
.topbar{height:31px;background:var(--red);color:var(--white);font-size:11px}
.topbar .links{left:161px;top:9px;display:flex;gap:16px}
.topbar .links span::before{content:"";display:inline-block;width:8px;height:8px;border:1.5px solid var(--white);border-radius:2px;margin-right:5px;vertical-align:-1px}
.topbar .search{left:771px;top:6px;width:136px;height:19px;border:1px solid var(--white);border-radius:2px;font-size:10px;padding:3px 8px}
.topbar .search svg{position:absolute;right:6px;top:4px}
.topbar .cart{left:921px;top:8px;display:flex;align-items:center;gap:6px}
.topbar .cart i{width:15px;height:15px;border-radius:50%;background:var(--white);display:inline-block}

/* header */
.site-header{height:78px;background:var(--white)}
.brand{display:flex;align-items:center;gap:10px}
.brand .mark{width:52px;height:52px;background:var(--red);border-radius:6px}
.brand .name{font-family:var(--head);font-weight:700;font-size:27px;color:var(--ink);line-height:1}
.site-header .brand{left:161px;top:13px}
.nav{left:566px;top:31px;display:flex;gap:27px;font-family:var(--head);font-size:13px;font-weight:400;text-transform:uppercase}

/* hero */
.hero{height:533px;background:linear-gradient(160deg,#22a9d8 0%,#1697c6 100%)}
.hero .product{left:157px;top:58px;width:400px;height:420px;border-radius:6px;background:linear-gradient(135deg,#d9d9d9 0%,#5e6470 45%,#15171b 100%)}
.hero .brand{left:637px;top:110px;gap:14px}
.hero .brand .mark{width:74px;height:74px;background:var(--white);border-radius:10px}
.hero .brand .name{color:var(--white);font-size:48px}
.hero h1{left:560px;width:502px;top:252px;text-align:center;font-family:var(--head);font-weight:700;font-size:32px;color:var(--white);text-transform:uppercase}
.hero .sub{left:560px;width:502px;top:296px;text-align:center;font-size:12.5px;font-weight:500;color:var(--white);text-transform:uppercase}
.btn-outline{border:2px solid var(--white);color:var(--white);font-family:var(--head);font-weight:700;text-transform:uppercase;display:flex;align-items:center;justify-content:center}
.hero .btn-outline{left:744px;top:351px;width:140px;height:40px;font-size:16px}

/* promo strip */
.promo{height:397px}
.promo .tile{top:0;height:397px}
.promo .off{left:0;width:410px;background:linear-gradient(150deg,#d7d7d7 0%,#c0533a 45%,#b5301a 100%)}
.promo .guarantee{left:410px;width:395px;background:var(--green);color:var(--white);text-align:center}
.promo .save{left:805px;width:395px;background:linear-gradient(160deg,#d6d6d6 0%,#a8aaae 50%,#2c2f36 100%)}
.promo .big{font-family:var(--body);font-weight:900}
.off .big{position:absolute;right:32px;top:48px;font-size:80px;color:var(--red);line-height:1}
.off .small{position:absolute;right:58px;top:126px;font-family:var(--head);font-size:23px;color:var(--ink)}
.guarantee svg{margin-top:46px}
.guarantee .big{font-size:54px;line-height:1;margin-top:18px}
.guarantee p{font-family:var(--body);font-weight:700;font-size:21px;line-height:31px;margin-top:14px;text-transform:uppercase}
.guarantee .btn-dark{margin:30px auto 0;width:156px;height:50px;background:var(--ink);color:var(--white);font-weight:700;font-size:19px;display:flex;align-items:center;justify-content:center}
.save .big{position:absolute;left:31px;top:42px;font-size:80px;color:#1e9ad6;line-height:1}
.save .small{position:absolute;left:81px;top:113px;font-family:var(--head);font-size:30px;color:var(--ink)}

/* section titles */
.section-title{position:absolute;left:0;width:1200px;text-align:center;font-family:var(--head);font-weight:700;font-size:38px;text-transform:uppercase;color:var(--ink)}
.title-rule{position:absolute;left:480px;width:240px;height:2px;background:#9a9a9a}
.title-rule::after{content:"";position:absolute;left:92px;top:-1px;width:56px;height:4px;background:var(--red)}

/* features */
.features{height:826px;background:linear-gradient(135deg,#f7f7f7 0%,#ececec 40%,#fafafa 70%,#e9e9e9 100%)}
.features .section-title{top:52px}
.features .title-rule{top:107px}
.features svg.diagram{position:absolute;left:0;top:0}
.diagram text{font-family:var(--body);font-size:14px;letter-spacing:2px;fill:#333;text-transform:uppercase}

/* customize band */
.customize{height:125px;background:var(--red)}
.customize h2{left:161px;top:42px;font-family:var(--body);font-weight:700;font-size:35px;color:var(--white);text-transform:uppercase;letter-spacing:-.3px}
.customize .btn-outline{left:861px;top:47px;width:179px;height:40px;font-size:14px;gap:6px}

/* featured products */
.featured{height:498px}
.featured .section-title{top:48px}
.featured .title-rule{top:96px}
.card{top:144px;width:203px}
.card .photo{height:203px;background:var(--grey);display:flex;align-items:center;justify-content:center}
.card .photo div{width:146px;height:118px;border-radius:6px}
.card .meta{height:65px;background:var(--grey-mid);display:flex;align-items:center;justify-content:space-between;padding:0 22px}
.card .price{font-family:var(--body);font-weight:700;font-size:18px}
.card .stars{color:var(--red);font-size:14px;letter-spacing:1px}
.card .stars b{color:#9a9a9a;font-weight:400}
.card .shop{height:35px;background:var(--ink);color:var(--white);font-weight:700;font-size:13px;display:flex;align-items:center;justify-content:center;gap:5px}
.arrow{top:271px;width:46px;height:46px;border-radius:50%;background:#d8d8d8;display:flex;align-items:center;justify-content:center}

/* steps */
.steps{height:255px}
.step{top:31px;width:278px;height:177px;display:flex;align-items:center;padding-left:30px;gap:20px;color:var(--white)}
.step .icon{width:106px;height:90px;border-radius:4px;background:rgba(255,255,255,.28);flex:none}
.step span{font-family:var(--head);font-weight:300;font-size:31px;line-height:32px}
.step.green{left:161px;background:var(--green)}
.step.yellow{left:462px;background:var(--yellow)}
.step.red{left:761px;background:var(--red)}

/* newsletter */
.newsletter{height:86px;background:var(--sky);color:var(--white)}
.newsletter h3{left:161px;top:24px;font-family:var(--body);font-weight:700;font-size:18px;text-transform:uppercase}
.newsletter p{left:264px;top:46px;font-size:15px}
.newsletter .field{left:504px;top:25px;width:395px;height:33px;background:var(--white);color:#a3a3a3;font-size:11px;display:flex;align-items:center;padding-left:14px;gap:10px}
.newsletter .field i{width:14px;height:10px;background:#9a9a9a;display:inline-block;border-radius:1px}
.newsletter .go{left:899px;top:25px;width:141px;height:33px;background:var(--ink);font-size:13px;font-weight:700;display:flex;align-items:center;justify-content:center}

/* footer */
.site-footer{height:241px;background:var(--dark);color:var(--muted)}
.badge{left:161px;top:46px;width:230px;height:159px;background:#d7d7d7;border:2px solid #9da0a6;text-align:center;color:var(--ink)}
.badge .seal{width:82px;height:82px;border-radius:50%;background:#2c2f36;margin:6px auto 8px;border:4px solid #8b8e95}
.badge h4{font-size:10px;font-weight:900;text-transform:uppercase}
.badge p{font-size:8.5px;line-height:12px;margin:4px 14px 0}
.col h5{font-family:var(--body);font-weight:700;font-size:13px;color:var(--white);text-transform:uppercase;margin-bottom:22px}
.col ul{list-style:none;font-size:11px}
.col li{height:23px}
.col li::before{content:"";display:inline-block;border-left:4px solid var(--muted);border-top:3px solid transparent;border-bottom:3px solid transparent;margin-right:8px}
.col.quick{left:474px;top:48px}
.col.service{left:654px;top:46px}
.col.service li{height:26px}
.col.contact{left:863px;top:48px}
.col.contact li{display:flex;gap:8px;height:auto;margin-bottom:9px;line-height:15px}
.col.contact li::before{display:none}
.col.contact i{width:11px;height:11px;background:var(--white);border-radius:2px;flex:none;margin-top:2px}

/* bottom bar */
.bottombar{height:67px;background:var(--darker);color:var(--muted);border-top:1px solid #33363d}
.bottombar .copy{left:161px;top:26px;font-size:11px}
.bottombar .pay{left:540px;top:22px;display:flex;gap:6px}
.bottombar .pay span{width:28px;height:17px;background:#e9e9e9;border-radius:2px}
.bottombar .social{left:903px;top:20px;display:flex;gap:11px}
.bottombar .social span{width:26px;height:26px;border-radius:50%;border:1.5px solid var(--muted)}
</style>
</head>
<body>

<div class="topbar">
  <div class="abs links"><span>Log in</span><span>Register</span><span>My Account</span><span>Track my order</span></div>
  <div class="abs search">Search here...
    <svg width="10" height="10" viewBox="0 0 10 10"><circle cx="4" cy="4" r="3" fill="none" stroke="#fff" stroke-width="1.5"/><line x1="6.2" y1="6.2" x2="9" y2="9" stroke="#fff" stroke-width="1.5"/></svg>
  </div>
  <div class="abs cart"><i></i>Cart: 0 items - $0.00</div>
</div>

<header class="site-header">
  <div class="abs brand"><span class="mark"></span><span class="name">Bright Pouches</span></div>
  <nav class="abs nav"><span>Home</span><span>Listing</span><span>Product</span><span>Customize</span><span>Blog</span><span>Women's</span><span>Men's</span></nav>
</header>

<section class="hero">
  <div class="abs product" role="img" aria-label="Custom printed black leather wallet in front of its colourful gift box"></div>
  <div class="abs brand"><span class="mark"></span><span class="name">Bright Pouches</span></div>
  <h1 class="abs">Custom Printed Men's Wallets</h1>
  <p class="abs sub">High quality, durable leather, made to last</p>
  <div class="abs btn-outline">Shop Now!</div>
</section>

<section class="promo">
  <div class="abs tile off" role="img" aria-label="Close-up of a wallet printed with a red geometric pattern">
    <div class="big">20%</div>
    <div class="small">FLAT OFF</div>
  </div>
  <div class="abs tile guarantee">
    <svg width="64" height="58" viewBox="0 0 44 40" fill="none" stroke="#1e1f24" stroke-width="2.2"><rect x="3" y="12" width="36" height="25" rx="2"/><path d="M7 12 L30 3 L33 12"/><rect x="28" y="20" width="13" height="9" rx="1"/></svg>
    <div class="big">5 YEAR</div>
    <p>Money back guarantee<br>on wallet</p>
    <div class="btn-dark">SHOP NOW!</div>
  </div>
  <div class="abs tile save" role="img" aria-label="Open wallet filled with bank notes and cards">
    <div class="big">SAVE</div>
    <div class="small">45%</div>
  </div>
</section>

<section class="features">
  <h2 class="section-title">Features of our wallet</h2>
  <div class="title-rule"></div>
  <svg class="diagram" width="1200" height="826" viewBox="0 0 1200 826">
    <defs>
      <linearGradient id="photo" x1="0" y1="0" x2="1" y2="1"><stop offset="0" stop-color="#8d8f93"/><stop offset=".6" stop-color="#2a2c30"/><stop offset="1" stop-color="#111"/></linearGradient>
      <linearGradient id="box" x1="0" y1="0" x2="1" y2="1"><stop offset="0" stop-color="#e9e2d4"/><stop offset=".5" stop-color="#5f6672"/><stop offset="1" stop-color="#121315"/></linearGradient>
      <path id="a1" d="M297 330 A100 100 0 0 1 497 330"/>
      <path id="a2" d="M506 251 A100 100 0 0 1 706 251"/>
      <path id="a3" d="M715 330 A100 100 0 0 1 915 330"/>
      <path id="a4" d="M297 598 A100 100 0 0 1 497 598"/>
      <path id="a5" d="M506 675 A100 100 0 0 1 706 675"/>
      <path id="a6" d="M711 598 A100 100 0 0 1 911 598"/>
    </defs>
    <g stroke="#222" stroke-width="3" fill="none">
      <line x1="397" y1="463" x2="815" y2="463"/>
      <line x1="397" y1="416" x2="397" y2="514"/>
      <line x1="815" y1="416" x2="815" y2="514"/>
      <line x1="606" y1="337" x2="606" y2="393"/>
      <line x1="606" y1="533" x2="606" y2="589"/>
    </g>
    <g stroke="#111" stroke-width="4">
      <circle cx="397" cy="330" r="84" fill="url(#photo)" role="img" aria-label="Reinforced wallet corner close-up"/>
      <circle cx="606" cy="251" r="84" fill="url(#photo)" role="img" aria-label="Slim wallet profile"/>
      <circle cx="815" cy="330" r="84" fill="url(#photo)" role="img" aria-label="Leather grain texture"/>
      <circle cx="397" cy="598" r="84" fill="url(#photo)" role="img" aria-label="Coin compartment in use"/>
      <circle cx="606" cy="675" r="84" fill="url(#photo)" role="img" aria-label="Bank notes slid into note pocket"/>
      <circle cx="811" cy="598" r="84" fill="url(#photo)" role="img" aria-label="Cards in credit card slots"/>
    </g>
    <rect x="533" y="393" width="146" height="140" rx="6" fill="url(#box)" role="img" aria-label="Wallet with its gift box"/>
    <text><textPath href="#a1" startOffset="50%" text-anchor="middle">Reinforced corners</textPath></text>
    <text><textPath href="#a2" startOffset="50%" text-anchor="middle">Slim design - 15mm thick</textPath></text>
    <text><textPath href="#a3" startOffset="50%" text-anchor="middle">Durable luxury leather</textPath></text>
    <text><textPath href="#a4" startOffset="50%" text-anchor="middle">Two coin compartments</textPath></text>
    <text><textPath href="#a5" startOffset="50%" text-anchor="middle">Two note pockets</textPath></text>
    <text><textPath href="#a6" startOffset="50%" text-anchor="middle">Six credit card slots</textPath></text>
  </svg>
</section>

<section class="customize">
  <h2 class="abs">Customize your wallet now</h2>
  <div class="abs btn-outline">Customize now
    <svg width="13" height="13" viewBox="0 0 13 13"><circle cx="6.5" cy="6.5" r="6.5" fill="#fff"/><path d="M5 3.5 L8 6.5 L5 9.5" stroke="#ee4323" stroke-width="1.8" fill="none"/></svg>
  </div>
</section>

<section class="featured">
  <h2 class="section-title">Featured products</h2>
  <div class="title-rule"></div>
  <div class="abs arrow" style="left:88px"><svg width="12" height="14" viewBox="0 0 12 14"><path d="M8 2 L3 7 L8 12" stroke="#666" stroke-width="2.2" fill="none"/></svg></div>
  <div class="abs arrow" style="left:1069px"><svg width="12" height="14" viewBox="0 0 12 14"><path d="M4 2 L9 7 L4 12" stroke="#666" stroke-width="2.2" fill="none"/></svg></div>

  <div class="abs card" style="left:163px">
    <div class="photo"><div role="img" aria-label="Black wallet with white printed artwork" style="background:linear-gradient(135deg,#3a3c42,#0f1012)"></div></div>
    <div class="meta"><span class="price">$54.77</span><span class="stars">★★★★<b>★</b></span></div>
    <div class="shop">SHOP NOW <svg width="10" height="10" viewBox="0 0 10 10"><circle cx="5" cy="5" r="4" fill="none" stroke="#fff" stroke-width="1.3"/><path d="M4 3 L6 5 L4 7" stroke="#fff" stroke-width="1.3" fill="none"/></svg></div>
  </div>
  <div class="abs card" style="left:387px">
    <div class="photo"><div role="img" aria-label="Open wallet with notes and photo print inside" style="background:linear-gradient(135deg,#c9cbd0,#4b4e55 60%,#1a1b1e)"></div></div>
    <div class="meta"><span class="price">$64.77</span><span class="stars">★★★★<b>★</b></span></div>
    <div class="shop">SHOP NOW <svg width="10" height="10" viewBox="0 0 10 10"><circle cx="5" cy="5" r="4" fill="none" stroke="#fff" stroke-width="1.3"/><path d="M4 3 L6 5 L4 7" stroke="#fff" stroke-width="1.3" fill="none"/></svg></div>
  </div>
  <div class="abs card" style="left:612px">
    <div class="photo"><div role="img" aria-label="Wallet printed with red geometric pattern" style="background:linear-gradient(135deg,#e0552f,#a82410)"></div></div>
    <div class="meta"><span class="price">$64.77</span><span class="stars">★★★★<b>★</b></span></div>
    <div class="shop">SHOP NOW <svg width="10" height="10" viewBox="0 0 10 10"><circle cx="5" cy="5" r="4" fill="none" stroke="#fff" stroke-width="1.3"/><path d="M4 3 L6 5 L4 7" stroke="#fff" stroke-width="1.3" fill="none"/></svg></div>
  </div>
  <div class="abs card" style="left:836px">
    <div class="photo"><div role="img" aria-label="Plain black leather wallet" style="background:linear-gradient(135deg,#2c2e33,#0b0c0d)"></div></div>
    <div class="meta"><span class="price">$64.77</span><span class="stars">★★★★<b>★</b></span></div>
    <div class="shop">SHOP NOW <svg width="10" height="10" viewBox="0 0 10 10"><circle cx="5" cy="5" r="4" fill="none" stroke="#fff" stroke-width="1.3"/><path d="M4 3 L6 5 L4 7" stroke="#fff" stroke-width="1.3" fill="none"/></svg></div>
  </div>
</section>

<section class="steps">
  <div class="abs step green"><div class="icon" role="img" aria-label="Product selection illustration"></div><span>Chose<br>Products</span></div>
  <div class="abs step yellow"><div class="icon" role="img" aria-label="Account sign-in illustration"></div><span>Register/<br>Login</span></div>
  <div class="abs step red"><div class="icon" role="img" aria-label="Shopping cart illustration"></div><span>Checkout</span></div>
</section>

<section class="newsletter">
  <h3 class="abs">Subscribe to our newsletter</h3>
  <p class="abs">get 10% off your next order</p>
  <div class="abs field"><i></i>Your email address</div>
  <div class="abs go">SUBSCRIBE NOW!</div>
</section>

<footer class="site-footer">
  <div class="abs badge">
    <div class="seal"></div>
    <h4>5 Year money back guarantee on wallet</h4>
    <p>If you return your order within 30 days, we'll send your money back. No questions asked.</p>
  </div>
  <div class="abs col quick">
    <h5>Quick Links</h5>
    <ul><li>Home</li><li>Listing</li><li>Product</li><li>Customize</li><li>Men's</li></ul>
  </div>
  <div class="abs col service">
    <h5>Customer Service</h5>
    <ul><li>My account</li><li>Ship</li><li>Returns</li><li>FAQ</li></ul>
  </div>
  <div class="abs col contact">
    <h5>Contact Information</h5>
    <ul>
      <li><i style="border-radius:50% 50% 50% 0"></i>418 Harbor Lane, Fairview,<br>CA 90210</li>
      <li><i></i>hello@brightpouches.example</li>
      <li><i style="border-radius:50%"></i>123-456-7890</li>
      <li><i></i>123-456-7890</li>
    </ul>
  </div>
</footer>

<div class="bottombar">
  <div class="abs copy">© 2018 All Rights Reserved</div>
  <div class="abs pay"><span></span><span></span><span></span><span></span></div>
  <div class="abs social"><span></span><span></span><span></span><span></span></div>
</div>

</body>
</html>
```